New business needs it's first website designed and coded for Wordpress

This is a new website for a new business. The business is called The Remote Tech Specialist (TRTS). The business is based across multiple countries with the goal of providing workers in the Philippines opportunities to find work in international companies based in Australia, Singapore and New Zealand. The target market for TRTS is large enterprises (initially in Australia) looking for well legally structured business that knows how to recruit the top IT professionals and ensure that they are happy, all compliance, taxes and legals and professionally done and all services contracts are local to ensure enforceability.

We are looking for 10 pages (6 templates) for the website as follows:
Home
About Us
Services
Work from home full-timers
Work from office full-times
Work from home contractors
Work from office contractors
Careers Job Search
Employers Contact Us
Candidates Register your interest

Target Market(s)

IT Professionals in the Philippines & large enterprises in Australia, Singapore and New Zealand

Industry/Entity Type

IT Recruitment

Coding

Number of Pages Required

5+ page

Requirements
Must have
• Please based style off logo file attached.

```html
<!DOCTYPE html>
<html lang="en">
<head>
<meta charset="utf-8">
<title>The Remote Tech Specialist — Website Screens</title>
<link href="https://fonts.googleapis.com/css2?family=Ubuntu:wght@400;500;700&display=swap" rel="stylesheet">
<style>
:root{
  --band:#d4ecf4;
  --accent:#29a3d0;
  --ink:#1e1e1e;
  --muted:#a3a3a3;
  --bar:#b9b9b9;
  --bar-light:#e9e9e9;
  --pill:#eef6fa;
  --white:#ffffff;
}
*{margin:0;padding:0;box-sizing:border-box}
html,body{width:1200px;height:675px;overflow:hidden;background:var(--white)}
body{position:relative;font-family:"Ubuntu",sans-serif;color:var(--ink)}
.screen{position:absolute;width:379px;height:213px;background:var(--white);overflow:hidden}
.topbar{position:absolute;left:0;top:0;width:100%;height:7px;background:var(--bar)}
.topbar-sub{position:absolute;left:0;top:7px;width:100%;height:12px;background:var(--bar-light)}
.brand{position:absolute;left:20px;top:29px;display:flex;align-items:center;gap:3px;white-space:nowrap}
.brand-dot{width:5px;height:5px;border-radius:50%;background:var(--accent)}
.brand-name{font-size:6.2px;font-weight:700;color:var(--ink);line-height:1}
.search{position:absolute;left:122px;top:23px;width:103px;height:10px;border-radius:5px;background:var(--pill);box-shadow:1px 1px 1px rgba(0,0,0,.12);font-size:4.8px;font-weight:500;padding:2.4px 0 0 5px}
.nav span{position:absolute;top:41px;font-size:4.6px;color:var(--muted);white-space:nowrap}
.nav .active{color:var(--accent);font-weight:500}
.band{position:absolute;left:0;top:51px;width:100%;height:162px;background:var(--band)}
.notch{position:absolute;left:63px;top:51px}
.dropdown{position:absolute;left:186px;top:51px;width:74px}
.dropdown span{display:block;font-size:4.4px;color:var(--muted);line-height:7.4px;border-bottom:.5px solid #c9c9c9;white-space:nowrap}
.dropdown .active{color:var(--accent)}
.page-title{position:absolute;left:63px;top:80px;font-size:8.2px;font-weight:500;color:var(--accent);letter-spacing:.2px;white-space:nowrap}
.lead{position:absolute;left:63px;top:99px;width:254px;font-size:5.9px;line-height:6.7px;font-weight:500}
.frame{position:absolute;left:24px;top:119px}
.icon-slot{position:absolute;background:#e2f2f8;border-radius:2px}
.body-copy{position:absolute;left:66px;top:146px;width:250px;font-size:5.9px;line-height:6.7px;font-weight:500;text-align:center}
.lead.narrow{width:154px}
.login{position:absolute;left:224px;top:59px;width:124px;height:144px;background:var(--white);box-shadow:1px 1px 3px rgba(0,0,0,.25);font-size:3.6px;font-weight:500}
.login h3{position:absolute;top:5px;width:100%;text-align:center;font-size:5px;font-weight:700}
.social{position:absolute;top:14px;height:13px;background:#c6e2ee;font-size:3.6px;text-align:center;line-height:13px}
.or{position:absolute;width:100%;text-align:center}
.field-label{position:absolute;left:8px}
.field{position:absolute;left:52px;width:64px;height:8px;border:.5px solid #c9dfe8}
.btn-login{position:absolute;left:7px;top:82px;width:110px;height:11px;background:#20a0cf;color:var(--white);text-align:center;line-height:11px}
.btn-otp{position:absolute;left:7px;top:109px;width:110px;height:11px;border:.6px solid #20a0cf;text-align:center;line-height:11px}
.jobs{position:absolute;font-size:5.2px;font-weight:500;line-height:6px}
.jobs-head{color:var(--accent);font-weight:700}
.divider{position:absolute;left:189px;top:80px;width:.5px;height:110px;background:#a9c6d2}
</style>
</head>
<body>

<section class="screen" style="left:3px;top:103px">
  <div class="topbar"></div>
  <div class="brand"><span class="brand-dot"></span><span class="brand-name">The Remote Tech Specialist</span></div>
  <div class="search">Careers Job Search</div>
  <div class="band"></div>
  <nav class="nav"><span style="left:125px">Home</span><span style="left:151px">About Us</span><span class="active" style="left:186px">Services</span><span style="left:218px">Employers Contact Us</span><span style="left:283px">Candidates Register your interest</span></nav>
  <svg class="notch" width="24" height="21"><polygon points="0,0 24,0 12,21" fill="#fff"/></svg>
  <div class="dropdown"><span>Work from home full-timers</span><span class="active">Work from office full-times</span><span>Work from home contractors</span><span>Work from office contractors</span></div>
  <h2 class="page-title">Work from office full-times</h2>
  <p class="lead">Lorem ipsum dolor sit amet, consectetuer adipiscing elit, sed diam nonummy nibh euismod tincidunt ut laoreet dolore magna aliquam erat volutpat. Ut wisi enim ad minim veniam, quis nostrud exerci tation ullamcorper suscipit lobortis nisl ut aliquip ex ea commodo consequat. Duis autem vel eum iriure dolor in hendrerit in vulputate velit esse molestie consequat, vel illum dolore eu feugiat nulla facilisis at vero eros et accumsan et iusto odio dignissim qui blandit</p>
  <svg class="frame" width="66" height="78"><polygon points="1,1 64,39 1,77" fill="#fff" stroke="var(--accent)" stroke-width=".7"/></svg>
  <div class="icon-slot" role="img" aria-label="Line icon of an office desk workstation" style="left:32px;top:142px;width:24px;height:30px"></div>
  <p class="body-copy">Lorem ipsum dolor sit amet, consectetuer adipiscing elit, sed diam nonummy nibh euismod tincidunt ut laoreet dolore magna aliquam erat volutpat. Ut wisi enim ad minim veniam, quis nostrud exerci tation ullamcorper suscipit lobortis nisl ut aliquip ex ea commodo consequat. Duis autem vel eum iriure dolor in hendrerit in vulputate velit esse molestie consequat, vel illum dolore eu feugiat nulla facilisis at vero eros et accumsan et iusto odio dignissim qui blandit</p>
</section>

<section class="screen" style="left:411px;top:103px">
  <div class="topbar"></div>
  <div class="brand"><span class="brand-dot"></span><span class="brand-name">The Remote Tech Specialist</span></div>
  <div class="search">Careers Job Search</div>
  <div class="band"></div>
  <nav class="nav"><span style="left:125px">Home</span><span style="left:151px">About Us</span><span class="active" style="left:186px">Services</span><span style="left:218px">Employers Contact Us</span><span style="left:283px">Candidates Register your interest</span></nav>
  <svg class="notch" width="24" height="21"><polygon points="0,0 24,0 12,21" fill="#fff"/></svg>
  <div class="dropdown"><span>Work from home full-timers</span><span>Work from office full-times</span><span class="active">Work from home contractors</span><span>Work from office contractors</span></div>
  <h2 class="page-title">Work from home contractors</h2>
  <p class="lead">Lorem ipsum dolor sit amet, consectetuer adipiscing elit, sed diam nonummy nibh euismod tincidunt ut laoreet dolore magna aliquam erat volutpat. Ut wisi enim ad minim veniam, quis nostrud exerci tation ullamcorper suscipit lobortis nisl ut aliquip ex ea commodo consequat. Duis autem vel eum iriure dolor in hendrerit in vulputate velit esse molestie consequat, vel illum dolore eu feugiat nulla facilisis at vero eros et accumsan et iusto odio dignissim qui blandit</p>
  <svg class="frame" width="66" height="78"><polygon points="1,1 64,39 1,77" fill="#fff" stroke="var(--accent)" stroke-width=".7"/></svg>
  <div class="icon-slot" role="img" aria-label="Line icon of a house with a technician in a hard hat" style="left:32px;top:142px;width:24px;height:30px"></div>
  <p class="body-copy">Lorem ipsum dolor sit amet, consectetuer adipiscing elit, sed diam nonummy nibh euismod tincidunt ut laoreet dolore magna aliquam erat volutpat. Ut wisi enim ad minim veniam, quis nostrud exerci tation ullamcorper suscipit lobortis nisl ut aliquip ex ea commodo consequat. Duis autem vel eum iriure dolor in hendrerit in vulputate velit esse molestie consequat, vel illum dolore eu feugiat nulla facilisis at vero eros et accumsan et iusto odio dignissim qui blandit</p>
</section>

<section class="screen" style="left:816px;top:103px">
  <div class="topbar"></div>
  <div class="brand"><span class="brand-dot"></span><span class="brand-name">The Remote Tech Specialist</span></div>
  <div class="search">Careers Job Search</div>
  <div class="band"></div>
  <nav class="nav"><span style="left:125px">Home</span><span style="left:151px">About Us</span><span class="active" style="left:186px">Services</span><span style="left:218px">Employers Contact Us</span><span style="left:283px">Candidates Register your interest</span></nav>
  <svg class="notch" width="24" height="21"><polygon points="0,0 24,0 12,21" fill="#fff"/></svg>
  <div class="dropdown"><span>Work from home full-timers</span><span>Work from office full-times</span><span>Work from home contractors</span><span class="active">Work from office contractors</span></div>
  <h2 class="page-title">Work from office contractors</h2>
  <p class="lead">Lorem ipsum dolor sit amet, consectetuer adipiscing elit, sed diam nonummy nibh euismod tincidunt ut laoreet dolore magna aliquam erat volutpat. Ut wisi enim ad minim veniam, quis nostrud exerci tation ullamcorper suscipit lobortis nisl ut aliquip ex ea commodo consequat. Duis autem vel eum iriure dolor in hendrerit in vulputate velit esse molestie consequat, vel illum dolore eu feugiat nulla facilisis at vero eros et accumsan et iusto odio dignissim qui blandit</p>
  <svg class="frame" width="66" height="78"><polygon points="1,1 64,39 1,77" fill="#fff" stroke="var(--accent)" stroke-width=".7"/></svg>
  <div class="icon-slot" role="img" aria-label="Line icon of a technician at an office window" style="left:32px;top:142px;width:24px;height:30px"></div>
  <p class="body-copy">Lorem ipsum dolor sit amet, consectetuer adipiscing elit, sed diam nonummy nibh euismod tincidunt ut laoreet dolore magna aliquam erat volutpat. Ut wisi enim ad minim veniam, quis nostrud exerci tation ullamcorper suscipit lobortis nisl ut aliquip ex ea commodo consequat. Duis autem vel eum iriure dolor in hendrerit in vulputate velit esse molestie consequat, vel illum dolore eu feugiat nulla facilisis at vero eros et accumsan et iusto odio dignissim qui blandit</p>
</section>

<section class="screen" style="left:3px;top:379px">
  <div class="topbar"></div><div class="topbar-sub"></div>
  <div class="brand"><span class="brand-dot"></span><span class="brand-name">The Remote Tech Specialist</span></div>
  <div class="search">Careers Job Search</div>
  <div class="band"></div>
  <nav class="nav"><span style="left:125px">Home</span><span style="left:151px">About Us</span><span style="left:186px">Services</span><span class="active" style="left:218px">Employers Contact Us</span><span style="left:283px">Candidates Register your interest</span></nav>
  <svg class="notch" width="24" height="21"><polygon points="0,0 24,0 12,21" fill="#fff"/></svg>
  <h2 class="page-title">Employers Contact Us</h2>
  <p class="lead">Lorem ipsum dolor sit amet, consectetuer adipiscing elit, sed diam nonummy nibh euismod tincidunt ut laoreet dolore magna aliquam erat volutpat. Ut wisi enim ad minim veniam, quis nostrud exerci tation ullamcorper suscipit lobortis nisl ut aliquip ex ea commodo consequat. Duis autem vel eum iriure dolor in hendrerit in vulputate velit esse molestie consequat, vel illum dolore eu feugiat nulla facilisis at vero eros et accumsan et iusto odio dignissim qui blandit</p>
  <svg class="frame" width="66" height="78"><polygon points="1,1 64,39 1,77" fill="#fff" stroke="var(--accent)" stroke-width=".7"/></svg>
  <div class="icon-slot" role="img" aria-label="Line icon of two people" style="left:30px;top:146px;width:32px;height:24px"></div>
  <p class="body-copy">Lorem ipsum dolor sit amet, consectetuer adipiscing elit, sed diam nonummy nibh euismod tincidunt ut laoreet dolore magna aliquam erat volutpat. Ut wisi enim ad minim veniam, quis nostrud exerci tation ullamcorper suscipit lobortis nisl ut aliquip ex ea commodo consequat. Duis autem vel eum iriure dolor in hendrerit in vulputate velit esse molestie consequat, vel illum dolore eu feugiat nulla facilisis at vero eros et accumsan et iusto odio dignissim qui blandit</p>
</section>

<section class="screen" style="left:411px;top:379px">
  <div class="topbar"></div><div class="topbar-sub"></div>
  <div class="brand"><span class="brand-dot"></span><span class="brand-name">The Remote Tech Specialist</span></div>
  <div class="search">Careers Job Search</div>
  <div class="band"></div>
  <nav class="nav"><span style="left:125px">Home</span><span style="left:151px">About Us</span><span style="left:186px">Services</span><span style="left:218px">Employers Contact Us</span><span class="active" style="left:283px">Candidates Register your interest</span></nav>
  <svg class="notch" width="24" height="21"><polygon points="0,0 24,0 12,21" fill="#fff"/></svg>
  <h2 class="page-title">Candidates Register your interest</h2>
  <p class="lead narrow">Lorem ipsum dolor sit amet, consectetuer adipiscing elit, sed diam nonummy nibh euismod tincidunt ut laoreet dolore magna aliquam erat volutpat. Ut wisi enim ad minim veniam, quis nostrud exerci tation ullamcorper suscipit lobortis nisl ut aliquip ex ea commodo consequat. Duis autem vel eum iriure dolor in hendrerit in vulputate velit esse molestie consequat, vel illum dolore eu feugiat nulla facilisis at vero eros et accumsan et iusto odio dignissim qui blandit</p>
  <svg class="frame" width="66" height="78"><polygon points="1,1 64,39 1,77" fill="#fff" stroke="var(--accent)" stroke-width=".7"/></svg>
  <div class="icon-slot" role="img" aria-label="Line icon of a single person" style="left:34px;top:146px;width:18px;height:24px"></div>
  <div class="login">
    <h3>LOGIN WITH</h3>
    <div class="social" style="left:12px;width:23px">Email</div>
    <div class="social" style="left:41px;width:31px">Social</div>
    <div class="social" style="left:78px;width:33px">Network</div>
    <div class="or" style="top:33px">OR</div>
    <div class="field-label" style="top:47px">Enter Mobile/Email*</div>
    <div class="field" style="top:45px"></div>
    <div class="field-label" style="top:60px">Enter Password*</div>
    <div class="field" style="top:58px;left:42px;width:74px"><span style="position:absolute;right:5px;top:2px">Show</span></div>
    <div class="field-label" style="top:74px">Keep me signed in</div>
    <div style="position:absolute;right:10px;top:74px">Forgot Password?</div>
    <div class="btn-login">Login</div>
    <div class="or" style="top:100px">OR</div>
    <div class="btn-otp">Use OTP to Login</div>
    <div class="or" style="top:134px">New to Brightpath.com? &nbsp; Register Here</div>
  </div>
</section>

<section class="screen" style="left:816px;top:379px">
  <div class="topbar"></div><div class="topbar-sub"></div>
  <div class="brand"><span class="brand-dot"></span><span class="brand-name">The Remote Tech Specialist</span></div>
  <div class="search">Careers Job Search</div>
  <div class="band"></div>
  <nav class="nav"><span style="left:125px">Home</span><span style="left:151px">About Us</span><span style="left:186px">Services</span><span style="left:218px">Employers Contact Us</span><span style="left:283px">Candidates Register your interest</span></nav>
  <svg class="notch" width="24" height="21"><polygon points="0,0 24,0 12,21" fill="#fff"/></svg>
  <div class="jobs jobs-head" style="left:25px;top:81px">Recent jobsView</div>
  <div class="jobs jobs-head" style="left:157px;top:81px">All Jobs</div>
  <div class="divider"></div>
  <div class="jobs jobs-head" style="left:194px;top:81px">Number of Jobs in top citiesView</div>
  <div class="jobs jobs-head" style="left:331px;top:81px">All Jobs</div>

  <div class="jobs" style="left:25px;top:97px;width:158px">IT desktop support engineer, Nimbus Infotech , sfsfsfsfs</div>
  <div class="jobs" style="left:25px;top:112px;width:158px">Admin and HR Executive, Corvale Machinery pvt Ltd , sfsfsfsfs</div>
  <div class="jobs" style="left:25px;top:134px;width:162px">Data analayst, For a Client of Brightpath Staffing , sfsfsfs</div>
  <div class="jobs" style="left:25px;top:150px;width:158px">Technicians, Tradewell , sfsfsfsfs</div>
  <div class="jobs" style="left:25px;top:165px;width:150px">Desktop Support Engineer, For a Client of Brightpath Staffing , sfsfsfs</div>
  <div class="jobs" style="left:25px;top:187px;width:158px">It support engineers, For a Client of Brightpath Staffing , sfsfsfsfs</div>

  <div class="jobs" style="left:194px;top:97px">dfbsfdsfksf</div><div class="jobs" style="left:331px;top:97px">169</div>
  <div class="jobs" style="left:194px;top:112px">dfbsfdsfksf</div><div class="jobs" style="left:331px;top:112px">582</div>
  <div class="jobs" style="left:194px;top:127px">dfbsfdsfksf</div><div class="jobs" style="left:331px;top:127px">1000</div>
  <div class="jobs" style="left:194px;top:143px">dfbsfdsfksf</div><div class="jobs" style="left:331px;top:143px">642</div>
  <div class="jobs" style="left:194px;top:159px">dfbsfdsfksf</div><div class="jobs" style="left:331px;top:159px">499</div>
  <div class="jobs" style="left:194px;top:174px">dfbsfdsfksf</div><div class="jobs" style="left:331px;top:174px">855</div>
</section>

</body>
</html>
```